HL - business card

Harbor Lane Brokers is an insurance brokerage firm, inovative, proactive, vigorous, which aims to become the leader of the insurance brokers in Anfrica. We should like to get some designs which should be avoided also in Gray / Metallic for the Administration and Orange / Blue for the Managers (ike in the picture sent). The Blue / Green logo is not the correct one, but the source of the file. Please adjust the color accordingly for the business cards. 1 / Orange / Blue 2 / Gray / Metallic We want something classic but which is transmitted strenght, inovation, modernity and most of all, rapidity. We want something start-up like, very punchy and catching eye remaining profesional at the same time. Name: Tobias Wendell Function: Managing Director Address: N ° 17/18 Rua Dovel - R / C 2B Direita - Bairro Sambelo - Luanda Tel: (+244) 947 385 610 Email: tobias.wendell@harbor-l.com Website: www.harbor-l. com We want classic in the front and creative, colorfull at the back. The cards will be printed in relief, with very high quality of paper.
Insurance Broker
Designer to choose colors to be used in the design.

```html
<!DOCTYPE html>
<html lang="en">
<head>
<meta charset="utf-8">
<title>HL – Business Card</title>
<link href="https://fonts.googleapis.com/css2?family=Roboto:wght@400;700&display=swap" rel="stylesheet">
<style>
  :root {
    --backdrop: #dcdcdc;
    --card: #1e1f21;
    --card-deep: #18191b;
    --orange: #f0502d;
    --blue: #2eb4ea;
    --text: #d8d8d8;
    --divider: #55575a;
  }
  * { margin: 0; padding: 0; box-sizing: border-box; }
  html, body { width: 1200px; height: 801px; overflow: hidden; }
  body {
    background: var(--backdrop);
    font-family: "Roboto", Arial, sans-serif;
    position: relative;
  }
  .card {
    position: absolute;
    width: 540px;
    height: 308px;
    background: var(--card);
    border: 2px solid var(--orange);
    box-shadow: 0 10px 24px rgba(0,0,0,.25);
  }
  .card--front { left: 50px; top: 110px; }
  .card--back { left: 610px; top: 383px; }

  /* Front */
  .front-mark {
    position: absolute;
    left: 60px; top: 84px;
    width: 140px; height: 140px;
    display: flex; align-items: center; justify-content: center;
    gap: 12px;
  }
  .front-mark__dot {
    width: 26px; height: 26px; border-radius: 50%;
    background: var(--orange);
  }
  .front-mark__name {
    font-weight: 700; font-size: 44px; color: var(--blue);
  }
  .divider {
    position: absolute;
    left: 262px; top: 70px;
    width: 1px; height: 170px;
    background: var(--divider);
  }
  .contact {
    position: absolute;
    left: 286px; top: 70px;
    color: var(--text);
    font-size: 12.5px;
    line-height: 1.45;
  }
  .contact__name {
    color: var(--orange); font-weight: 700; font-size: 20px; line-height: 1.1;
  }
  .contact__role {
    color: var(--blue); font-size: 13.5px; margin-bottom: 8px;
  }
  .contact__address { margin-bottom: 12px; }
  .contact__line { display: flex; align-items: center; gap: 7px; }
  .contact__line svg { width: 11px; height: 11px; flex: none; }

  /* Back */
  .back-texture {
    position: absolute; inset: 0;
    background: radial-gradient(ellipse at 50% 45%, #262729 0%, var(--card-deep) 80%);
  }
  .back-brand {
    position: absolute;
    left: 0; right: 0; top: 126px;
    display: flex; align-items: center; justify-content: center; gap: 12px;
  }
  .back-brand__dot {
    width: 22px; height: 22px; border-radius: 50%;
    background: var(--orange);
  }
  .back-brand__name {
    color: var(--blue); font-weight: 700; font-size: 34px;
    text-transform: uppercase; letter-spacing: .5px;
  }
</style>
</head>
<body>
  <section class="card card--front" aria-label="Card front">
    <div class="front-mark">
      <span class="front-mark__dot"></span>
      <span class="front-mark__name">HL</span>
    </div>
    <div class="divider"></div>
    <div class="contact">
      <div class="contact__name">Tobias Wendell</div>
      <div class="contact__role">Managing Director</div>
      <div class="contact__address">
        N ° 17/18 Rua Dovel<br>
        R / C 2B Direita<br>
        Bairro Sambelo, Luanda
      </div>
      <div class="contact__line">
        <svg viewBox="0 0 12 12"><path d="M2.5 1l2 2.5-1 1.2c.7 1.5 1.8 2.6 3.3 3.3l1.2-1 2.5 2-1 2C5 10.8 1.2 7 1 2.5z" fill="#f0502d"/></svg>
        (+244) 947 385 610
      </div>
      <div class="contact__line">
        <svg viewBox="0 0 12 12"><rect x="1" y="2.5" width="10" height="7" fill="#f0502d"/><path d="M1 2.5l5 4 5-4" stroke="#1e1f21" fill="none"/></svg>
        tobias.wendell@harbor-l.com
      </div>
      <div class="contact__line">
        <svg viewBox="0 0 12 12"><circle cx="6" cy="6" r="5" fill="#f0502d"/><path d="M1 6h10M6 1v10" stroke="#1e1f21" stroke-width=".8"/></svg>
        www.harbor-l.com
      </div>
    </div>
  </section>

  <section class="card card--back" aria-label="Card back">
    <div class="back-texture" role="img" aria-label="Subtle repeating emblem pattern in dark grey tones"></div>
    <div class="back-brand">
      <span class="back-brand__dot"></span>
      <span class="back-brand__name">Harbor Lane Brokers</span>
    </div>
  </section>
</body>
</html>
```